Business Card for Makeup Artist

I need a business card designed for my makeup and hair artistry business which is primarily events and weddings focused. The card needs to be sleek, simple, stylish and appealing to women. I would prefer a white background but open to suggestions also. I also love the marble background look. I have attached some example pics. It needs to be a double sided card with logo and/or design on one side and contact details in the centre of the card on the other side. NO LOGO ON BACK. Examples attached.

Target Market(s)

Females age 14-55

Industry/Entity Type

Business

Contact Information for Business Card

Nora Vint
Principal Makeup Artist
P: 0413 925 214
E: nora@lumirabeauty.com.au
W: www.lumirabeauty.com.au

Requirements
Should not have
• No yellow, green, red or blue in the design.

```html
<!DOCTYPE html>
<html lang="en">
<head>
<meta charset="utf-8">
<title>Lumira Makeup Artistry – Business Card</title>
<link rel="stylesheet" href="https://fonts.googleapis.com/css2?family=Josefin+Slab:wght@400&family=Questrial&family=Montserrat:wght@400&display=swap">
<style>
  :root {
    --backdrop: #9a9a9a;
    --card: #fbfbfa;
    --ink: #4a4a4a;
    --pink: #d2449b;
    --pink-soft: #f3c9e2;
    --shadow: rgba(0, 0, 0, 0.22);
  }
  * { margin: 0; padding: 0; box-sizing: border-box; }
  html, body {
    width: 1200px;
    height: 900px;
    overflow: hidden;
    background: var(--backdrop);
  }
  .canvas {
    position: relative;
    width: 1200px;
    height: 900px;
  }
  .card {
    position: absolute;
    left: 280px;
    width: 640px;
    height: 390px;
    background: var(--card);
    box-shadow: 0 6px 18px var(--shadow);
  }
  .card--front { top: 40px; }
  .card--back { top: 470px; }

  /* Front: brand name */
  .brand {
    position: absolute;
    left: 0;
    right: 0;
    top: 128px;
    text-align: center;
    color: var(--ink);
  }
  .brand__name {
    display: block;
    font-family: "Josefin Slab", serif;
    font-weight: 400;
    font-size: 84px;
    line-height: 1;
    letter-spacing: 2px;
  }
  .brand__tagline {
    display: block;
    margin-top: 10px;
    font-family: "Questrial", sans-serif;
    font-size: 24px;
    letter-spacing: 1px;
  }

  /* Back: frame and corner ornaments */
  .frame {
    position: absolute;
    inset: 0;
  }
  .ornament {
    position: absolute;
    width: 74px;
    height: 74px;
    background: radial-gradient(circle at center, var(--pink-soft), rgba(243, 201, 226, 0.35));
    border-radius: 6px;
  }
  .ornament--tl { top: 14px; left: 14px; }
  .ornament--tr { top: 14px; right: 14px; }
  .ornament--bl { bottom: 14px; left: 14px; }
  .ornament--br { bottom: 14px; right: 14px; }

  /* Back: contact details */
  .details {
    position: absolute;
    left: 0;
    right: 0;
    top: 112px;
    text-align: center;
    color: var(--ink);
  }
  .details__name {
    font-family: "Josefin Slab", serif;
    font-weight: 400;
    font-size: 60px;
    line-height: 1;
    letter-spacing: 3px;
    text-transform: uppercase;
  }
  .details__role {
    margin-top: 4px;
    font-family: "Montserrat", sans-serif;
    font-size: 15px;
    letter-spacing: 1.5px;
    color: var(--pink);
    text-transform: uppercase;
  }
  .details__phone {
    margin-top: 8px;
    display: flex;
    align-items: center;
    justify-content: center;
    gap: 12px;
    font-family: "Questrial", sans-serif;
    font-size: 17px;
    letter-spacing: 1px;
  }
  .details__phone::before,
  .details__phone::after {
    content: "";
    width: 70px;
    height: 1px;
    background: var(--ink);
  }
  .details__line {
    margin-top: 4px;
    font-family: "Questrial", sans-serif;
    font-size: 17px;
    letter-spacing: 0.5px;
  }
</style>
</head>
<body>
<main class="canvas">

  <section class="card card--front" aria-label="Card front">
    <div class="brand">
      <span class="brand__name">Lumira</span>
      <span class="brand__tagline">MAKEUP ARTISTRY</span>
    </div>
  </section>

  <section class="card card--back" aria-label="Card back">
    <svg class="frame" width="640" height="390" viewBox="0 0 640 390" aria-hidden="true">
      <g stroke="#d2449b" stroke-width="1.5">
        <line x1="100" y1="30" x2="540" y2="30"/>
        <line x1="100" y1="360" x2="540" y2="360"/>
        <line x1="30" y1="100" x2="30" y2="290"/>
        <line x1="610" y1="100" x2="610" y2="290"/>
      </g>
    </svg>
    <div class="ornament ornament--tl" role="img" aria-label="Pink filigree corner ornament"></div>
    <div class="ornament ornament--tr" role="img" aria-label="Pink filigree corner ornament"></div>
    <div class="ornament ornament--bl" role="img" aria-label="Pink filigree corner ornament"></div>
    <div class="ornament ornament--br" role="img" aria-label="Pink filigree corner ornament"></div>

    <div class="details">
      <h1 class="details__name">Nora Vint</h1>
      <p class="details__role">Principal Makeup Artist</p>
      <p class="details__phone">0413 925 214</p>
      <p class="details__line">nora@lumirabeauty.com.au</p>
      <p class="details__line">www.lumirabeauty.com.au</p>
    </div>
  </section>

</main>
</body>
</html>
```